Insurance Law Website

**Please note do not sell insurance, we are a law firm which specialises in Insurance law.**

We are a legal insurance firm based in Australia consisting of 150+ legal professionals.

Our initial budget for this project is around: $500

We require a design to meet the specification below, however we do want designers to come up with an interpretation of something modern but still professional, we need it to stand out above all other legal websites!

1. Responsive design
2. It should be a minimalist design, the use of background imagery is fine but we are looking to de-clutter the home page in particular and have additional content accessible through menu links to other areas such as publications, news, announcements and expert/staff pages, careers etc.
3. Something that stands out from a typical legal website.
4. The homepage should cater for a video which will contain a 'who we are' message from the CEO/Firm.
5. Colours used light/medium blues (eg: #8aabff, #bdd7fc), white
6. We also require a static information box on the page with the heading "THREE STATES, ONE FOCUS" - see image attached for full text of the box.

Visitors to our website should be aware we are an Insurance law firm, this can be achieved by using insurance focused full background imagery (no natural disasters such as floods, earthquakes etc) such as insurance buildings (Harwick building - London), international landmarks etc

Some websites we like certain aspects of;

http://pellambraithwaite.com/ - top image boxes
http://www.vantel.com.au/ - similar however prefer to use a FULL background image, with one full width text box at the bottom, navigation menu at the top with logo

However please don't take these examples as a sign of what the site MUST look like, please use your imagination to interpret your own vision.

Reason: Extended due to feedback provided and waiting for resubmission of designs. It appears that some people may be misunderstanding the brief, please review the brief in full before submitting any designs and let us know if you have any questions.

Reason: Apologies to those who are waiting for a decision we are reviewing and discussiing all submitted designs internally and waiting for some additional amendments to come in. We have extended the project a final time whilst we carry out our reviews. Please continue to submit any modifications and thanks again for everyone's input thus far. D+T

We have 3 days left of this project please keep submitting your designs. This is a guaranteed project.

D+T

Target Market(s)

Lawyers looking for publications, information, contact details of our lawyers and careers/job searches.

Industry/Entity Type

Insurance

Font styles to use
Sans Serif

Requirements
Must have
• Top menu to include:

Home (small icon)
Who We Are (text)
Experts (text)
Expertise (text)
Media (text)
- News (text)
- Publications (text)
Community Footprint (text)
Careers (text)
Contact (text/icon)
Search (icon - will expand on click to search in field)

Footer to include:

Copyright (text)
Privacy Policy (text)
Cookie policy (text)
Sitemap (text)
Contact (text/icon)
Chainbook (icon)
Print (icon)
Email (icon)

Should not have
• Stereotypical imagery such as legal scales, money bags, natural disasters etc. We are a professional firm and require designs to suit.

```html
<!DOCTYPE html>
<html lang="en">
<head>
<meta charset="utf-8">
<title>Dalton Thorne — Insurance Law</title>
<link rel="stylesheet" href="https://fonts.googleapis.com/css2?family=Pathway+Gothic+One&family=Open+Sans:wght@400&family=PT+Sans:wght@400&display=swap">
<style>
  :root {
    --blue-deep: #0a4597;
    --blue-nav-top: #1c63c0;
    --blue-nav-bottom: #073f8c;
    --blue-heading: #1552a8;
    --blue-light: #8aabff;
    --blue-pale: #bdd7fc;
    --text-grey: #8a8a8a;
    --text-dark: #5c5c5c;
    --white: #ffffff;
    --line: #e3e3e3;
  }
  * { margin: 0; padding: 0; box-sizing: border-box; }
  html, body { width: 1200px; height: 1143px; overflow: hidden; background: var(--white); }
  body { position: relative; font-family: "Pathway Gothic One", sans-serif; }

  .brand {
    position: absolute; left: 132px; top: 38px;
    font-family: "Open Sans", sans-serif; font-weight: 400;
    color: var(--blue-deep); font-size: 30px; line-height: 28px; letter-spacing: 0.5px;
  }
  .brand span { display: block; }
  .brand span:first-child { padding-left: 16px; }

  .search {
    position: absolute; left: 888px; top: 71px; width: 182px; height: 24px;
    background: #f3f3f3; border: 1px solid #e6e6e6;
    font-size: 13px; color: #a9a9a9; padding: 4px 4px; display: flex; justify-content: space-between; align-items: center;
  }

  .hero {
    position: absolute; left: 0; top: 133px; width: 1200px; height: 526px;
    background:
      radial-gradient(ellipse at 55% 10%, #d9dde0 0%, rgba(200,205,210,0) 35%),
      linear-gradient(90deg, #2c3236 0%, #4a5559 25%, #8d9296 45%, #5c6265 60%, #8e8c86 80%, #3f4648 100%);
  }

  .main-nav {
    position: absolute; left: 131px; top: 104px; width: 939px; height: 59px;
    display: flex;
    background: linear-gradient(180deg, var(--blue-nav-top) 0%, var(--blue-nav-bottom) 100%);
  }
  .main-nav a {
    display: flex; align-items: center; justify-content: center; gap: 9px; white-space: nowrap;
    color: var(--white); text-decoration: none; font-size: 21px;
    border-right: 1px solid rgba(0,30,80,0.55); box-shadow: inset -1px 0 0 rgba(255,255,255,0.12);
  }
  .main-nav a:last-child { border-right: none; box-shadow: none; }

  .section-title {
    position: absolute; top: 688px; font-size: 21px; font-weight: 400; color: var(--blue-heading);
    white-space: nowrap;
  }

  .focus-box {
    position: absolute; left: 128px; top: 726px; width: 462px; height: 323px; overflow: hidden;
    border: 1px solid var(--line);
    background: linear-gradient(115deg, #eef0f3 0%, #ffffff 18%, #c9ccd4 45%, #e9eaee 75%, #ffffff 100%);
    padding: 14px 16px 0 12px; font-family: "PT Sans", sans-serif;
  }
  .focus-box h2 { font-weight: 400; color: #1f64b8; font-size: 50px; line-height: 64px; letter-spacing: -0.5px; white-space: nowrap; }
  .focus-box p { margin-top: 10px; font-size: 24px; line-height: 33px; color: var(--text-dark); }
  .focus-box p span { display: block; white-space: nowrap; text-align: justify; text-align-last: justify; }
  .focus-box em { font-style: normal; color: var(--blue-light); }

  .video {
    position: absolute; left: 611px; top: 726px; width: 460px; height: 271px;
    background: linear-gradient(180deg, #5d6ad8 0%, #7f8be6 35%, #b58ad0 58%, #3e4fb0 75%, #2a3d96 100%);
  }
  .video-controls {
    position: absolute; left: 0; bottom: 0; width: 100%; height: 26px; background: #1b1b1b;
    color: #dcdcdc; font-size: 9px; font-family: Arial, sans-serif;
  }
  .video-progress { position: absolute; left: 0; top: -4px; width: 100%; height: 4px; background: #555; }
  .video-progress i { position: absolute; left: 0; top: 0; height: 4px; width: 108px; background: #c81b1b; }

  .intro {
    position: absolute; left: 611px; top: 997px; width: 462px;
    font-size: 15px; line-height: 30px; color: var(--text-grey);
  }
  .intro span { display: block; white-space: nowrap; }
  .intro a { color: var(--blue-heading); text-decoration: none; font-size: 17px; }

  .site-footer {
    position: absolute; left: 0; top: 1080px; width: 1200px; height: 63px; background: var(--blue-deep);
    color: var(--white);
  }
  .legal {
    position: absolute; left: 138px; top: 20px; display: flex; align-items: center; font-size: 17px; white-space: nowrap;
  }
  .legal small { font-size: 14px; }
  .legal .sep { margin: 0 9px; }
  .footer-tools {
    position: absolute; left: 912px; top: 23px; display: flex; align-items: center; gap: 6px; font-size: 17px; white-space: nowrap;
  }
  .tool-square {
    width: 26px; height: 26px; background: var(--white); display: flex; align-items: center; justify-content: center;
  }
</style>
</head>
<body>

<header>
  <div class="brand"><span>dalton</span><span>thorne</span></div>
  <div class="search">Search
    <svg width="10" height="10" viewBox="0 0 10 10"><circle cx="4" cy="4" r="3" fill="none" stroke="#999" stroke-width="1.2"/><line x1="6.2" y1="6.2" x2="9" y2="9" stroke="#999" stroke-width="1.4"/></svg>
  </div>
</header>

<div class="hero" role="img" aria-label="Upward view of a steel and glass office tower with external lift shafts"></div>

<nav class="main-nav">
  <a href="#" style="width:100px">
    <svg width="18" height="16" viewBox="0 0 18 16"><path d="M9 1 L17 8 H14.5 V15 H10.5 V10.5 H7.5 V15 H3.5 V8 H1 Z" fill="#fff"/></svg>HOME</a>
  <a href="#" style="width:117px">WHO WE ARE</a>
  <a href="#" style="width:88px">EXPERTS</a>
  <a href="#" style="width:105px">EXPERTISE</a>
  <a href="#" style="width:80px">MEDIA</a>
  <a href="#" style="width:60px">NEWS</a>
  <a href="#" style="width:120px">PUBLICATIONS</a>
  <a href="#" style="width:176px">COMMUNITY FOOTPRINT</a>
  <a href="#" style="width:93px">CAREERS</a>
</nav>

<h1 class="section-title" style="left:129px">WELCOME TO DALTON THORNE</h1>
<h1 class="section-title" style="left:610px">WHO WE ARE ?</h1>

<section class="focus-box">
  <h2>Three states.<br>One focus.</h2>
  <p>
    <span>Our sole focus is <em>insurance law</em> and</span>
    <span>we act for a diverse range of risk</span>
    <span>carriers, underwriting agents, brokers</span>
    <span>and corporate insureds relevant to</span>
    <span>litigious and general advisory services.</span>
  </p>
</section>

<section class="video" role="img" aria-label="Video still of a city riverside skyline at dusk">
  <svg style="position:absolute;left:203px;top:103px" width="46" height="46" viewBox="0 0 46 46">
    <circle cx="23" cy="23" r="22" fill="#2a2a2a" stroke="#e8e8e8" stroke-width="2"/>
    <path d="M17 13 L33 23 L17 33 Z" fill="#fff"/>
  </svg>
  <div class="video-controls">
    <div class="video-progress"><i></i></div>
    <svg style="position:absolute;left:104px;top:-8px" width="12" height="12"><circle cx="6" cy="6" r="5" fill="#ddd" stroke="#999"/></svg>
    <svg style="position:absolute;left:16px;top:9px" width="8" height="10"><rect width="3" height="10" fill="#ccc"/><rect x="5" width="3" height="10" fill="#ccc"/></svg>
    <svg style="position:absolute;left:48px;top:8px" width="16" height="12"><path d="M0 4 H4 L9 0 V12 L4 8 H0 Z" fill="#ccc"/><path d="M11 3 Q14 6 11 9" stroke="#ccc" fill="none"/></svg>
    <span style="position:absolute;left:72px;top:8px"><b style="color:#fff">0:02</b> / 0:10</span>
    <span style="position:absolute;left:390px;top:8px">720p</span>
    <svg style="position:absolute;left:420px;top:8px" width="12" height="11"><path d="M1 4 H10 L7 1 M11 7 H2 L5 10" stroke="#ccc" fill="none" stroke-width="1.3"/></svg>
    <svg style="position:absolute;left:442px;top:7px" width="11" height="11"><path d="M0 4 V0 H4 M7 0 H11 V4 M11 7 V11 H7 M4 11 H0 V7" stroke="#ccc" fill="none" stroke-width="1.5"/></svg>
  </div>
</section>

<p class="intro">
  <span>Lorem Ipsum is simply dummy text of the printing and typesetting industry. Lorem Ipsum has been</span>
  <span>the industry's standard dummy text ever since the 1500s of type and scrambled... <a href="#">Read More</a></span>
</p>

<footer class="site-footer">
  <div class="legal">
    <small>Copyright ©2013 Company Name &nbsp;- All rights reserved</small>
    <span class="sep" style="margin:0 14px">|</span>
    <span>Privacy Policy</span><span class="sep">|</span>
    <span>Cookie policy</span><span class="sep">|</span>
    <span>Sitemap</span>
  </div>
  <div class="footer-tools">
    <svg width="12" height="16" viewBox="0 0 12 16"><path d="M2 1 L5 1 L6 5 L4 6.5 Q5.5 10 8 11.5 L9.5 9.5 L12 11 L11 15 Q4 15 1 6 Z" fill="#fff"/></svg>
    <span style="margin-right:8px">Contact</span>
    <span style="margin-right:2px">Chainbook</span>
    <span class="tool-square" aria-label="Print">
      <svg width="18" height="16" viewBox="0 0 18 16"><rect x="4" y="0" width="10" height="5" fill="#0a4597"/><rect x="0" y="5" width="18" height="7" rx="1" fill="#0a4597"/><rect x="4" y="9" width="10" height="7" fill="#fff" stroke="#0a4597" stroke-width="1.5"/></svg>
    </span>
    <span class="tool-square" aria-label="Email">
      <svg width="18" height="13" viewBox="0 0 18 13"><rect width="18" height="13" fill="#0a4597"/><path d="M1 1 L9 7 L17 1" stroke="#fff" stroke-width="1.5" fill="none"/></svg>
    </span>
  </div>
</footer>

</body>
</html>
```